Verpackungen für kleine Imkerei
Zielgruppe
Wir sind eine kleine Imkerei aus dem Aargau (Schweiz) und stellen zusammen mit unseren glücklichen Bienen feinsten Honig her. Gerne möchten wir unseren visuelle Kommunikation nach aussen mit Hilfe eines neuen Etiketts verbessern.
Aufgabenstellung
Das Etikett muss rechteckig sein und wir auf einem runden Glas aufgeklebt. Die Maximalgrösse ist 210x45mm (beim 500g Glas) und entsprechend kleiner bei kleineren Einheiten. Wir möchten ein Grunddesign, welches adaptierbar ist auf die weiteren Sorten. (Waldhonig, Blütenhonig, cremiger Blütenhonig, Zürcher Stadthonig, Badener Stadthonig, Lenzburger Stadthonig). Barcode muss keinen eingefügt werden, nur die gesetzlichen Daten müssen auf dem Etiektt stehen. Weitere Wünsche und Anmerkungen befinden sich im pdf.
Sollten Dateien oder Bilder nachgereicht werden, bitte melden!

```html
<!DOCTYPE html>
<html lang="de">
<head>
<meta charset="utf-8">
<title>Honigetiketten Waldhonig</title>
<link rel="stylesheet" href="https://fonts.googleapis.com/css2?family=Montserrat:wght@300;400;600;700;800&display=swap">
<style>
  :root {
    --paper: #ece6dc;
    --white: #ffffff;
    --placeholder: rgba(255, 255, 255, 0.22);
    --lilac-bg: #c9a3cd;
    --lilac-ink: #6a2a8c;
    --lilac-wash-a: #7c4cb0;
    --lilac-wash-b: #b8468f;
    --leaf-bg: #a3cb72;
    --leaf-ink: #3e5a1f;
    --leaf-wash-a: #2f8a22;
    --leaf-wash-b: #4fa533;
  }
  * { box-sizing: border-box; margin: 0; padding: 0; }
  html, body { width: 1200px; height: 667px; overflow: hidden; }
  body {
    background: var(--paper);
    font-family: "Montserrat", sans-serif;
    position: relative;
  }
  .label {
    position: absolute;
    left: 72px;
    width: 1057px;
    height: 229px;
    overflow: hidden;
    color: var(--white);
  }
  .label--lilac { top: 85px; background: var(--lilac-bg); --ink: var(--lilac-ink); --wash-a: var(--lilac-wash-a); --wash-b: var(--lilac-wash-b); }
  .label--leaf { top: 354px; background: var(--leaf-bg); --ink: var(--leaf-ink); --wash-a: var(--leaf-wash-a); --wash-b: var(--leaf-wash-b); }

  .label__wash {
    position: absolute;
    left: 255px; top: -10px;
    width: 610px; height: 250px;
    background:
      radial-gradient(ellipse 45% 55% at 40% 55%, var(--wash-a) 0%, transparent 75%),
      radial-gradient(ellipse 45% 60% at 68% 45%, var(--wash-b) 0%, transparent 75%);
    opacity: .85;
  }
  .label__mascot {
    position: absolute;
    background: var(--placeholder);
    border-radius: 6px;
  }
  .label__mascot--left { left: 130px; top: 30px; width: 128px; height: 32px; }
  .label__mascot--center { left: 614px; top: 14px; width: 36px; height: 28px; }

  .care { position: absolute; left: 28px; top: 70px; width: 250px; }
  .care__title { font-size: 12.7px; font-weight: 700; color: var(--ink); margin-bottom: 7px; }
  .care__text { font-size: 12.5px; font-weight: 300; line-height: 16px; margin-bottom: 16px; }

  .title-block { position: absolute; left: 383px; width: 300px; top: 0; text-align: center; }
  .brand { position: absolute; left: 0; right: 0; top: 42px; font-size: 26px; font-weight: 600; }
  .product {
    position: absolute; left: -40px; right: -40px; top: 100px;
    font-size: 47px; font-weight: 800; letter-spacing: .5px;
    text-shadow: 2px 3px 5px rgba(0,0,0,.35);
  }
  .title-rule { position: absolute; left: 81px; width: 137px; top: 169px; height: 2px; background: var(--white); }
  .origin { position: absolute; left: 0; right: 0; top: 182px; font-size: 19px; font-weight: 400; }

  .weight { position: absolute; right: 148px; top: 175px; text-align: right; font-size: 12.7px; line-height: 16px; font-weight: 400; }
  .weight strong { font-weight: 700; }

  .divider { position: absolute; left: 933px; top: 20px; width: 2px; height: 186px; background: var(--white); }
  .producer {
    position: absolute; left: 950px; bottom: 23px; height: 200px;
    writing-mode: vertical-rl; transform: rotate(180deg);
    font-style: normal;
    font-size: 11.5px; line-height: 17px; font-weight: 300;
  }
  .producer__name { font-weight: 700; font-size: 13px; }
  .producer__web { font-weight: 700; color: var(--ink); font-size: 13px; }
</style>
</head>
<body>

  <section class="label label--lilac">
    <div class="label__wash" role="img" aria-label="Aquarellfläche mit Wabenmuster in Violett und Magenta"></div>
    <div class="label__mascot label__mascot--left" role="img" aria-label="Illustration einer fliegenden Biene mit Flugbahn"></div>
    <div class="label__mascot label__mascot--center" role="img" aria-label="Illustration einer kleinen Biene"></div>

    <div class="care">
      <p class="care__title">Honig von glücklichen Bienen</p>
      <p class="care__text">Honig gut verschlossen,<br>kühl (max. 15°), dunkel<br>und trocken lagern.</p>
      <p class="care__text">Mindesthaltbarkeitsdatum<br>und Los Nr. befinden sich<br>auf dem Glasboden.</p>
    </div>

    <div class="title-block">
      <p class="brand">Summwiese</p>
      <h1 class="product">WALDHONIG</h1>
      <div class="title-rule"></div>
      <p class="origin">Honig aus Aargau</p>
    </div>

    <p class="weight">Nettogewicht<br><strong>500 g</strong></p>
    <div class="divider"></div>
    <address class="producer">
      <span class="producer__name">M. &amp; S. Karrigo</span><br>
      Lindenrain 4<br>
      5600 Wiesental<br>
      Tel. 01234 56 78 90<br>
      <span class="producer__web">www.summwiese.ch</span>
    </address>
  </section>

  <section class="label label--leaf">
    <div class="label__wash" role="img" aria-label="Aquarellfläche mit Wabenmuster in Grüntönen"></div>
    <div class="label__mascot label__mascot--left" role="img" aria-label="Illustration einer fliegenden Biene mit Flugbahn"></div>
    <div class="label__mascot label__mascot--center" role="img" aria-label="Illustration einer kleinen Biene"></div>

    <div class="care">
      <p class="care__title">Honig von glücklichen Bienen</p>
      <p class="care__text">Honig gut verschlossen,<br>kühl (max. 15°), dunkel<br>und trocken lagern.</p>
      <p class="care__text">Mindesthaltbarkeitsdatum<br>und Los Nr. befinden sich<br>auf dem Glasboden.</p>
    </div>

    <div class="title-block">
      <p class="brand">Summwiese</p>
      <h1 class="product">WALDHONIG</h1>
      <div class="title-rule"></div>
      <p class="origin">Honig aus Aargau</p>
    </div>

    <p class="weight">Nettogewicht<br><strong>500 g</strong></p>
    <div class="divider"></div>
    <address class="producer">
      <span class="producer__name">M. &amp; S. Karrigo</span><br>
      Lindenrain 4<br>
      5600 Wiesental<br>
      Tel. 01234 56 78 90<br>
      <span class="producer__web">www.summwiese.ch</span>
    </address>
  </section>

</body>
</html>
```